Business card - house cleaning company

We want friendly high end business card highlighting our services . NO LOGOs on back of card please.. no vertical cards NO DOUBLE BROOMS

2 owners of the company: Corinne Halvey & Joel Brandt

Included phone number: (555)318-2047

Email: brightlanetidy@mailnest.example

Website: www.brightlanetidy.example

Bonded & Insured

Larkspur Falls, CO 80599

Slogan maybe: Bringing a brighter shine to every corner of home

We want elegant high end card for house cleaning service. Maybe 2 sided if needed. Can it have bullet points of some services we offer

Residential Home Cleaning
Vacation Rental Cleaning
Commercial Cleaning
Carpet Cleaning
Window Cleaning
Property Management
Property Inspections
Property Maintenance
Trash Removal
Concierge Services

Highlight service on back of card. If we can do a one sided card with all this that’s great as well. Not cartoony.

Our logo attached and a design somone I had Perrin but they put very little time in. Not Unique enough. If you can do a custom design with a feminine touch that be great.

You will be eliminated for not reading the brief. NO DOUBLE LOGOS NO DOUBLE BROOMS. PLEASE BE CREATIVE. IF POST SAME LOGO WITH SMAL CHANGES RHEY WILL BE ELIMINATED. BE CREATIVE.

Thank you everyone for your designs. please only use the logo 1 time. and would love to see some that dont look all the same. We appreciate your time.

Target Market(s)

Residential and vacation rental home cleaning maid service

Industry/Entity Type

House cleaning maid services

Contact Information for Business Card

For business card use logo. black and green one provided. others for example. I wil try find some example.. We want friendly high end look. 2 owners of the company: Corinne Halvey & Joel Brandt Included phone number: (555)318-2047 Email: brightlanetidy@mailnest.example Website: www.brightlanetidy.example Bonded & Insured Estes Park, CO Slogan maybe: Bringing a brighter shine to every corner of home or Quality Service Guaranteed We want elegant high end card for house cleaning service. Maybe 2 sided if needed. Can it have bullet points of some services we offer Residential Home Cleaning Vacation Rental Cleaning Commercial Cleaning Carpet Cleaning Window Cleaning Property Management Property Inspections Property Maintenance Trash Removal Concierge Services

Requirements
Must have
• For business card use logo . Creativity. black and green one provided. We want friendly high end look. 2 owners of the company: Corinne Halvey & Joel Brandt Included phone number: (555)318-2047 Email: brightlanetidy@mailnest.example Website: www.brightlanetidy.example Licensed Bonded & Insured Estes Park, CO Slogan maybe: Bringing a brighter shine to every corner of home or Quality Service Guaranteed We want elegant high end card for house cleaning service. Maybe 2 sided if needed. Can it have bullet points of some services we offer Residential Home Cleaning Vacation Rental Cleaning Commercial Cleaning Carpet Cleaning Window Cleaning Property Management Property Inspections Property Maintenance Trash Removal Concierge Services .. creatitivty a plus. whimsical. we like stars..
Nice to have
• we want much better than the example of biz card provided as example. logo has colors that are in our website palette as well. We are open to ideas for the business card design. Will pay tip to best work. PLEASE USE COMPLIMENTING COLORS. . WE LIKE BLACK AND WHITE, stars
Should not have
• NO DOUBLE LOGOS. READ READ. READ. YOU WILL BE ELIMINATED no double logos or double brooms same side of card. I want didfrent examples. please don't make all your submission look the same

```html
<!DOCTYPE html>
<html lang="en">
<head>
<meta charset="utf-8">
<title>Bright Lane Tidy – Business Card</title>
<link rel="stylesheet" href="https://fonts.googleapis.com/css2?family=Arimo:wght@400;700&family=Raleway:wght@700;800&display=swap">
<style>
  :root {
    --backdrop: #dcdcdc;
    --ink: #1b1b1b;
    --paper: #ffffff;
    --night: #0b0b0b;
    --night-soft: #262626;
    --leaf: #6f9a3f;
    --leaf-dark: #4d6e2a;
    --mist: #eaeaea;
  }
  * { box-sizing: border-box; margin: 0; padding: 0; }
  html, body { width: 1200px; height: 900px; overflow: hidden; }
  body {
    background: var(--backdrop);
    font-family: "Arimo", Arial, sans-serif;
    color: var(--ink);
    position: relative;
  }
  .card {
    position: absolute;
    width: 700px;
    height: 400px;
    border-radius: 4px;
    overflow: hidden;
    box-shadow: 0 6px 18px rgba(0,0,0,.25);
  }

  /* Back side */
  .card-back {
    left: 170px; top: 35px;
    background: linear-gradient(115deg, var(--night) 0%, var(--night) 60%, var(--night-soft) 72%, var(--night) 84%);
  }
  .back-decoration {
    position: absolute;
    left: 0; top: 170px;
    width: 470px; height: 230px;
    background: radial-gradient(ellipse at 45% 70%, rgba(77,110,42,.55) 0%, rgba(77,110,42,.18) 45%, rgba(0,0,0,0) 75%);
  }
  .service-list {
    position: absolute;
    right: 34px; top: 42px;
    list-style: none;
    text-align: right;
  }
  .service-list li {
    color: var(--paper);
    font-size: 20px;
    line-height: 31px;
    display: flex;
    justify-content: flex-end;
    align-items: center;
    gap: 14px;
  }
  .service-list svg { width: 22px; height: 22px; flex: none; }

  /* Front side */
  .card-front {
    left: 330px; top: 465px;
    background: var(--paper);
  }
  .brand {
    position: absolute;
    left: 0; right: 0; top: 52px;
    text-align: center;
    font-family: "Raleway", Arial, sans-serif;
    font-weight: 800;
    font-size: 44px;
    letter-spacing: .5px;
    color: var(--ink);
  }
  .broom-art {
    position: absolute;
    left: 318px; top: 128px;
    width: 64px; height: 192px;
    background: linear-gradient(180deg, var(--mist) 0%, #cfcfcf 100%);
    border-radius: 4px;
  }
  .owners {
    position: absolute;
    left: 40px; top: 200px;
    width: 260px;
    text-align: center;
    font-family: "Raleway", Arial, sans-serif;
    font-weight: 700;
    font-size: 27px;
    line-height: 34px;
    color: var(--leaf);
  }
  .contact {
    position: absolute;
    left: 402px; top: 140px;
    width: 280px;
    list-style: none;
  }
  .contact li {
    display: flex;
    align-items: center;
    gap: 12px;
    font-size: 16px;
    line-height: 28px;
    color: #2b2b2b;
    white-space: nowrap;
  }
  .contact svg { width: 16px; height: 16px; flex: none; fill: var(--leaf); }
  .credentials {
    position: absolute;
    left: 402px; top: 272px;
    font-size: 18px;
  }
  .credentials .label { color: var(--leaf); }
  .credentials strong { font-weight: 700; color: var(--ink); }
  .slogan-band {
    position: absolute;
    left: 0; right: 0; bottom: 0;
    height: 58px;
    background: var(--leaf);
    display: flex;
    align-items: center;
    justify-content: center;
    font-family: "Raleway", Arial, sans-serif;
    font-weight: 800;
    font-size: 20px;
    letter-spacing: .6px;
    text-transform: uppercase;
    color: var(--ink);
  }
</style>
</head>
<body>

<section class="card card-back" aria-label="Back of card: services">
  <div class="back-decoration" role="img" aria-label="Faint mountain silhouette with sparkling stars"></div>
  <ul class="service-list">
    <li>Residential Home Cleaning <svg viewBox="0 0 20 20"><path d="M10 0 L11.6 8.4 L20 10 L11.6 11.6 L10 20 L8.4 11.6 L0 10 L8.4 8.4 Z" fill="#6f9a3f"/></svg></li>
    <li>Vacation Rental Cleaning <svg viewBox="0 0 20 20"><path d="M10 0 L11.6 8.4 L20 10 L11.6 11.6 L10 20 L8.4 11.6 L0 10 L8.4 8.4 Z" fill="#6f9a3f"/></svg></li>
    <li>Commercial Cleaning <svg viewBox="0 0 20 20"><path d="M10 0 L11.6 8.4 L20 10 L11.6 11.6 L10 20 L8.4 11.6 L0 10 L8.4 8.4 Z" fill="#6f9a3f"/></svg></li>
    <li>Carpet Cleaning <svg viewBox="0 0 20 20"><path d="M10 0 L11.6 8.4 L20 10 L11.6 11.6 L10 20 L8.4 11.6 L0 10 L8.4 8.4 Z" fill="#6f9a3f"/></svg></li>
    <li>Window Cleaning <svg viewBox="0 0 20 20"><path d="M10 0 L11.6 8.4 L20 10 L11.6 11.6 L10 20 L8.4 11.6 L0 10 L8.4 8.4 Z" fill="#6f9a3f"/></svg></li>
    <li>Property Management <svg viewBox="0 0 20 20"><path d="M10 0 L11.6 8.4 L20 10 L11.6 11.6 L10 20 L8.4 11.6 L0 10 L8.4 8.4 Z" fill="#6f9a3f"/></svg></li>
    <li>Property Inspections <svg viewBox="0 0 20 20"><path d="M10 0 L11.6 8.4 L20 10 L11.6 11.6 L10 20 L8.4 11.6 L0 10 L8.4 8.4 Z" fill="#6f9a3f"/></svg></li>
    <li>Property Maintenance <svg viewBox="0 0 20 20"><path d="M10 0 L11.6 8.4 L20 10 L11.6 11.6 L10 20 L8.4 11.6 L0 10 L8.4 8.4 Z" fill="#6f9a3f"/></svg></li>
    <li>Trash Removal <svg viewBox="0 0 20 20"><path d="M10 0 L11.6 8.4 L20 10 L11.6 11.6 L10 20 L8.4 11.6 L0 10 L8.4 8.4 Z" fill="#6f9a3f"/></svg></li>
    <li>Concierge Services <svg viewBox="0 0 20 20"><path d="M10 0 L11.6 8.4 L20 10 L11.6 11.6 L10 20 L8.4 11.6 L0 10 L8.4 8.4 Z" fill="#6f9a3f"/></svg></li>
  </ul>
</section>

<section class="card card-front" aria-label="Front of card: contact">
  <h1 class="brand">Bright Lane Tidy</h1>
  <div class="broom-art" role="img" aria-label="Upright broom with small sparkles at the bristles"></div>
  <p class="owners">Corinne Halvey &amp;<br>Joel Brandt</p>
  <ul class="contact">
    <li><svg viewBox="0 0 16 16"><path d="M8 1 L15 7.5 H13 V15 H9.5 V10.5 H6.5 V15 H3 V7.5 H1 Z"/></svg>Larkspur Falls, CO 80599</li>
    <li><svg viewBox="0 0 16 16"><path d="M4 1 L6.5 4.5 L5 6.3 C6 8.4 7.6 10 9.7 11 L11.5 9.5 L15 12 L13.3 14.6 C7.5 14.3 1.7 8.5 1.4 2.7 Z"/></svg>555 318 2047</li>
    <li><svg viewBox="0 0 16 16"><path d="M1 3 H15 V13 H1 Z M1.8 3.8 L8 8.8 L14.2 3.8" fill="none" stroke="#6f9a3f" stroke-width="1.5"/></svg>brightlanetidy@mailnest.example</li>
    <li><svg viewBox="0 0 16 16"><circle cx="8" cy="8" r="7"/></svg>www.brightlanetidy.example</li>
  </ul>
  <p class="credentials"><span class="label">Licensed:</span> <strong>Bonded &amp; Insured</strong></p>
  <div class="slogan-band">Bringing a brighter shine to every corner of home</div>
</section>

</body>
</html>
```